Logo and packaging for Electronic Disposable Shisha
We are a new company launching a Disposable Electronic Shisha that last up to 600 puff that comes in different colours and flavour as: blueberry, strawberry,apple, chocolate, and fruit mix . The logo should communicate elegance, style life and gold as the one color only . The name is ZEFO (e-shisha) , The idea is having the logo on capital letter and e-shiha at the footer of the logo,Could be just letters or letters and logo You guys are the experts so please show me your creativity! The product will come in 2 presentation,on individual tube as in the image and "cigarette box style with 5 eshishas" We need the design of the logo and packaging of the cigarette package,on the package the logo and edges will be on gold stamping and should contain all the flavours (blueberry,strawberry,apple,chocolate and mint) You can play with the color of the background and images. Thank You!
+18
Cigarette
ZEFO (e-shisha)

```html
<!DOCTYPE html>
<html lang="en">
<head>
<meta charset="utf-8">
<title>ZEFO E-Shisha Packaging</title>
<link rel="stylesheet" href="https://fonts.googleapis.com/css2?family=Montserrat:wght@400;500&display=swap">
<style>
  :root {
    --bg: #ffffff;
    --pack-light: #f7f7f7;
    --pack-shade: #dcdcdc;
    --pack-edge: #3a3a3a;
    --frame: #c8b8a3;
    --band: #ededed;
    --berry: #9b0057;
    --apple: #80b642;
    --orange: #f05a22;
    --ghost: #d8d6de;
  }
  html, body {
    margin: 0;
    padding: 0;
    overflow: hidden;
    background: var(--bg);
  }
  .canvas {
    position: relative;
    width: 1200px;
    height: 1200px;
    background: var(--bg);
    font-family: "Montserrat", sans-serif;
  }
  .pack {
    position: absolute;
    width: 339px;
    height: 525px;
  }
  .pack--berry  { left: 33px;  top: 48px;  --accent: var(--berry); }
  .pack--apple  { left: 426px; top: 258px; --accent: var(--apple); }
  .pack--orange { left: 810px; top: 615px; --accent: var(--orange); }
  .pack svg { display: block; width: 100%; height: 100%; }
  .pack .accent { fill: var(--accent); }
  .pack .wordmark {
    fill: var(--accent);
    font-family: "Montserrat", sans-serif;
    font-weight: 500;
    font-size: 38px;
    letter-spacing: 4px;
  }
  .pack .tagline {
    fill: #8a8a8a;
    font-family: "Montserrat", sans-serif;
    font-weight: 400;
    font-size: 8.5px;
    letter-spacing: 2px;
  }
  .pack .label-text {
    fill: #ffffff;
    font-family: "Montserrat", sans-serif;
    font-weight: 400;
    font-size: 9px;
    letter-spacing: 1px;
  }
  .ghost-name {
    position: absolute;
    left: 80px;
    top: 960px;
    margin: 0;
    font-family: "Montserrat", sans-serif;
    font-weight: 500;
    font-size: 150px;
    line-height: 1;
    letter-spacing: 22px;
    color: var(--ghost);
  }
</style>
</head>
<body>
<main class="canvas">

  <svg width="0" height="0" style="position:absolute">
    <defs>
      <linearGradient id="pack-surface" x1="0" x2="1" y1="0" y2="0">
        <stop offset="0" stop-color="#e6e6e6"/>
        <stop offset="0.15" stop-color="#f7f7f7"/>
        <stop offset="0.85" stop-color="#f4f4f4"/>
        <stop offset="1" stop-color="#dedede"/>
      </linearGradient>
    </defs>
  </svg>

  <!-- Reusable pack structure, one per flavour colour -->
  <div class="pack pack--berry">
    <svg viewBox="0 0 226 350">
      <rect x="0" y="0" width="226" height="103" rx="4" fill="url(#pack-surface)"/>
      <rect x="0" y="103" width="226" height="247" fill="url(#pack-surface)"/>
      <line x1="0" y1="103" x2="226" y2="103" stroke="#cfcfcf" stroke-width="1.5"/>
      <rect x="0" y="346" width="226" height="4" fill="var(--pack-edge)"/>
      <rect x="15" y="13" width="199" height="77" rx="14" fill="none" stroke="var(--frame)" stroke-width="2"/>
      <rect class="accent" x="56" y="42" width="114" height="26"/>
      <text class="label-text" x="113" y="58.5" text-anchor="middle">HSGDHFGDJ</text>
      <rect x="15" y="113" width="203" height="225" rx="14" fill="none" stroke="var(--frame)" stroke-width="2"/>
      <rect class="accent" x="23" y="123" width="187" height="205" rx="12"/>
      <rect x="23" y="190" width="187" height="71" fill="var(--band)"/>
      <text class="wordmark" x="116" y="236" text-anchor="middle">ZEFO</text>
      <text class="tagline" x="116" y="252" text-anchor="middle">E-SHISHA</text>
    </svg>
  </div>

  <div class="pack pack--apple">
    <svg viewBox="0 0 226 350">
      <rect x="0" y="0" width="226" height="103" rx="4" fill="url(#pack-surface)"/>
      <rect x="0" y="103" width="226" height="247" fill="url(#pack-surface)"/>
      <line x1="0" y1="103" x2="226" y2="103" stroke="#cfcfcf" stroke-width="1.5"/>
      <rect x="0" y="346" width="226" height="4" fill="var(--pack-edge)"/>
      <rect x="15" y="13" width="199" height="77" rx="14" fill="none" stroke="var(--frame)" stroke-width="2"/>
      <rect class="accent" x="56" y="42" width="114" height="26"/>
      <text class="label-text" x="113" y="58.5" text-anchor="middle">HSGDHFGDJ</text>
      <rect x="15" y="113" width="203" height="225" rx="14" fill="none" stroke="var(--frame)" stroke-width="2"/>
      <rect class="accent" x="23" y="123" width="187" height="205" rx="12"/>
      <rect x="23" y="190" width="187" height="71" fill="var(--band)"/>
      <text class="wordmark" x="116" y="236" text-anchor="middle">ZEFO</text>
      <text class="tagline" x="116" y="252" text-anchor="middle">E-SHISHA</text>
    </svg>
  </div>

  <div class="pack pack--orange">
    <svg viewBox="0 0 226 350">
      <rect x="0" y="0" width="226" height="103" rx="4" fill="url(#pack-surface)"/>
      <rect x="0" y="103" width="226" height="247" fill="url(#pack-surface)"/>
      <line x1="0" y1="103" x2="226" y2="103" stroke="#cfcfcf" stroke-width="1.5"/>
      <rect x="0" y="346" width="226" height="4" fill="var(--pack-edge)"/>
      <rect x="15" y="13" width="199" height="77" rx="14" fill="none" stroke="var(--frame)" stroke-width="2"/>
      <rect class="accent" x="56" y="42" width="114" height="26"/>
      <text class="label-text" x="113" y="58.5" text-anchor="middle">HSGDHFGDJ</text>
      <rect x="15" y="113" width="203" height="225" rx="14" fill="none" stroke="var(--frame)" stroke-width="2"/>
      <rect class="accent" x="23" y="123" width="187" height="205" rx="12"/>
      <rect x="23" y="190" width="187" height="71" fill="var(--band)"/>
      <text class="wordmark" x="116" y="236" text-anchor="middle">ZEFO</text>
      <text class="tagline" x="116" y="252" text-anchor="middle">E-SHISHA</text>
    </svg>
  </div>

  <p class="ghost-name">ZEFO</p>

</main>
</body>
</html>
```